Glow & Keepsakes Swap Meet – November 2025 Marketing Design

We need a flyer/wireframe design for our upcoming Glow & Keepsakes Swap Meet on Sunday, November 9, 2025, from 10:00 AM – 2:00 PM at Tubelight Restoration Works, Greenleaf, WI.

This is a casual, community-style event with free admission for both vendors and attendees. The design should work for both print and digital marketing. The focus is on authentic neon signs, beer signs & memorabilia, and collectible advertising items. While our past flyer highlighted jukeboxes and arcade games, this new design should emphasize:

A wide variety of neon signs

Beer memorabilia and advertising collectibles

Repair services (encouraging attendees to bring in broken neon signs for free assessments)

The look should be fun, bold, and eye-catching, appealing to both serious collectors and those looking to sell or downsize their collections. The design should clearly communicate that this is a unique, lively collectors’ event centered around neon culture.

Target Market(s)

Collectors and enthusiasts of neon signs, beer memorabilia, and vintage advertising Hobbyists and antique seekers looking to browse, buy, or trade Casual sellers and collectors who may only have a few items they’d like to part with and connect with others

Industry/Entity Type

Events / Collectibles / Antiques & Memorabilia

Font styles to use
Other font styles liked:
• Bright, bold, neon-inspired colors (reds, blues, yellows, oranges). Retro palette welcome but with fresh clean layout that pops both in print and digital.

Colors
0054AA
0677BA
7BADD7
CADEEF
E8F1F8
FFF300
FFF600
FEFA6F
FFFEC7
FFFEE8
F0912C
F2A743
F7CA91
FBE8D2
FDF5EE
EB3D1F
EC4F4E
F09395
F8D3D4
FCEDEE

Requirements
Must have
• Event details: Sunday, November 9, 2025, from 10 AM – 2 PM Location: 5182 Old Mill Creek Road, Greenleaf, WI Contact info: info@tubelightworks.example | Call/Text 920-555-0172 Social media: “Like and follow Tubelight Restoration Works on Facebook for updates” Food and drinks available for purchase on-site Free admission for attendees AND free setup for vendors Vendor note: “$40 refundable deposit required to hold your spot; refunded once set up” Callout to bring broken neon signs for free repair assessments Clear messaging that this event is designed both for people attending and collectors who want to set up and sell/trade Highlight that this is our second event — the first was well attended and had positive feedback Must be usable for both print and digital marketing Must look completely different from the first flyer design attatched
Nice to have
• Retro-inspired, bold design that emphasizes neon and beer memorabilia culture (not jukebox/arcade-heavy) Tagline or headline that captures both sides (e.g., “Browse • Buy • Sell • Trade” or “For Collectors, By Collectors”) Icons or visuals of neon signs, beer memorabilia, and advertising items Small callout that this is a casual, collector-focused event — the right place for people with even just a few items to connect with others
Should not have
• Re-use of the last flyer’s jukebox-heavy style, fonts, or layout Too much emphasis on arcade/pinball (secondary focus at most) Overly cluttered design that makes vendor vs. attendee info unclear

```html
<!DOCTYPE html>
<html lang="en">
<head>
<meta charset="utf-8">
<title>Glow &amp; Keepsakes Swap Meet – Flyer</title>
<link rel="stylesheet" href="https://fonts.googleapis.com/css2?family=Montserrat:wght@300;500;600;700;800;900&family=Nunito:wght@800;900&display=swap">
<style>
  :root {
    --ink: #000000;
    --paper: #ffffff;
    --band-pink: #ff4a88;
    --lime: #2ef01a;
    --red: #ef3636;
    --blue: #1e88e5;
    --yellow: #ffd200;
    --frame-yellow: #fff300;
    --neon-core: #fffec7;
    --orange: #ff8c00;
    --pink-text: #ff4a88;
    --cyan: #20d6f0;
  }
  * { box-sizing: border-box; margin: 0; padding: 0; }
  html, body { width: 927px; height: 1200px; overflow: hidden; background: var(--ink); }
  .flyer {
    position: relative; width: 927px; height: 1200px; background: var(--ink);
    font-family: "Montserrat", sans-serif; color: var(--paper); overflow: hidden;
  }
  .abs { position: absolute; }
  .top-band {
    left: 0; top: 0; width: 927px; height: 64px; background: var(--band-pink);
    display: flex; align-items: center; justify-content: center;
    color: var(--lime); font-weight: 500; font-size: 30px; letter-spacing: 4.6px; white-space: nowrap;
  }
  .event-date { left: 0; width: 927px; top: 88px; text-align: center; font-size: 32px; font-weight: 600; }
  .event-time { left: 0; width: 927px; top: 124px; text-align: center; font-size: 23px; font-weight: 500; }
  .title-plate {
    left: 96px; top: 174px; width: 735px; height: 81px; background: var(--red); border-radius: 18px;
    display: flex; align-items: center; justify-content: center;
  }
  .title-glow {
    font-size: 56px; font-weight: 800; color: var(--neon-core); letter-spacing: 0.5px;
    text-shadow: 0 0 4px #ffe066, 0 0 10px var(--frame-yellow), 0 0 18px #ffb300;
  }
  .title-main {
    left: 0; width: 927px; top: 262px; text-align: center; font-size: 98px; font-weight: 800;
    color: var(--blue); line-height: 1; letter-spacing: 1px;
  }
  .address { left: 0; width: 927px; top: 368px; text-align: center; font-size: 31px; font-weight: 600; }
  .art-slot { border-radius: 10px; }
  .art-beer-sign { left: 130px; top: 428px; width: 145px; height: 178px; background: linear-gradient(160deg, #f0912c 0%, #1e88e5 55%, #2ef01a 100%); opacity: .55; }
  .art-bowling { left: 395px; top: 446px; width: 135px; height: 140px; background: linear-gradient(180deg, #ffffff 0%, #fff300 100%); opacity: .45; }
  .art-patio { left: 645px; top: 462px; width: 152px; height: 108px; background: linear-gradient(135deg, #20d6f0 0%, #ec4f4e 100%); opacity: .55; }
  .info-box {
    top: 621px; height: 144px; border: 5px solid var(--frame-yellow); border-radius: 28px;
  }
  .repair-box { left: 92px; width: 306px; }
  .repair-icon { left: 21px; top: 25px; width: 56px; height: 86px; }
  .repair-text {
    left: 80px; top: 10px; width: 212px; text-align: center; font-size: 19.5px; font-weight: 600;
    line-height: 23.5px; letter-spacing: .3px;
  }
  .repair-text .accent { color: var(--blue); }
  .features-box { left: 463px; width: 371px; }
  .feature-list { list-style: none; position: absolute; left: 30px; top: 9px; }
  .feature-list li { position: relative; padding-left: 25px; font-size: 22.5px; font-weight: 600; line-height: 27px; margin-bottom: 13px; letter-spacing: .3px; white-space: nowrap; }
  .feature-list li::before { content: ""; position: absolute; left: 0; top: 9px; width: 15px; height: 15px; border-radius: 50%; }
  .feature-list li.dot-yellow::before { background: var(--yellow); }
  .feature-list li.dot-blue::before { background: var(--blue); }
  .free-admission { left: 0; width: 927px; top: 795px; text-align: center; font-size: 89px; font-weight: 800; color: var(--yellow); line-height: 1; }
  .free-setup { left: 0; width: 927px; top: 880px; text-align: center; font-size: 52px; font-weight: 600; line-height: 1; letter-spacing: 1.5px; }
  .vendor-note { left: 40px; width: 331px; top: 960px; text-align: right; font-size: 26px; font-weight: 600; line-height: 29.6px; letter-spacing: .4px; }
  .vendor-note .lime { color: var(--lime); }
  .vendor-note .pink { color: var(--pink-text); }
  .vendor-note .fine { font-size: 22px; font-weight: 300; color: var(--pink-text); display: block; margin-top: 2px; }
  .social-square { left: 467px; top: 950px; width: 55px; height: 55px; background: var(--lime); border-radius: 9px; }
  .social-text { left: 467px; top: 945px; width: 450px; font-size: 26px; font-weight: 600; color: var(--orange); line-height: 30px; }
  .social-text .line-indent { display: block; padding-left: 66px; }
  .social-text .org { color: var(--lime); font-family: "Nunito", sans-serif; font-weight: 900; font-size: 22px; }
  .food { left: 536px; top: 1049px; font-size: 23px; font-weight: 600; line-height: 24px; letter-spacing: .5px; }
  .food small { display: block; font-size: 18px; letter-spacing: 0; }
  .contact-pill {
    left: 55px; top: 1113px; width: 817px; height: 64px; background: var(--red); border-radius: 30px;
    display: flex; align-items: center; justify-content: center;
    font-family: "Nunito", sans-serif; font-weight: 900; font-size: 26px; color: var(--ink);
  }
</style>
</head>
<body>
<main class="flyer">
  <header class="abs top-band">2nd Annual Glow &amp; Keepsakes Swap Meet</header>

  <p class="abs event-date">Sunday, November 9, 2025</p>
  <p class="abs event-time">10 am – 2 pm</p>

  <div class="abs title-plate"><h1 class="title-glow">GLOW &amp; KEEPSAKES</h1></div>
  <h2 class="abs title-main">SWAP MEET</h2>

  <p class="abs address">5182 Old Mill Creek Road, Greenleaf, WI</p>

  <div class="abs art-slot art-beer-sign" role="img" aria-label="Neon beer sign with parrot and palm trees"></div>
  <div class="abs art-slot art-bowling" role="img" aria-label="Neon outline of bowling pins and ball"></div>
  <div class="abs art-slot art-patio" role="img" aria-label="Neon Patio Open sign with palm tree"></div>

  <section class="abs info-box repair-box">
    <svg class="abs repair-icon" viewBox="0 0 56 86" aria-hidden="true">
      <g fill="none" stroke="#ffd200" stroke-width="2.6" stroke-linejoin="round">
        <path d="M38 4 L34 12 L40 17 L48 13 L50 20 L44 30 L38 30 L16 68 A10 10 0 1 1 8 62 L30 24 L28 16 Z"/>
        <circle cx="11" cy="72" r="4"/>
      </g>
    </svg>
    <p class="abs repair-text">
      <span class="accent">BRING IN<br>YOUR BROKEN<br>NEON SIGNS FOR</span><br>FREE REPAIR<br>ASSESSMENTS
    </p>
  </section>

  <section class="abs info-box features-box">
    <ul class="feature-list">
      <li class="dot-yellow">Wide variety<br>of neon signs</li>
      <li class="dot-blue">Beer memorabilia &amp;<br>advertising collectibles</li>
    </ul>
  </section>

  <p class="abs free-admission">FREE ADMISSION</p>
  <p class="abs free-setup">FREE SETUP FOR VENDORS!</p>

  <p class="abs vendor-note">
    <span class="lime">$40 refundable<br>deposit </span><span class="pink">required<br>to hold your spot</span>
    <span class="fine">(refunded once set up)</span>
  </p>

  <div class="abs social-square" aria-hidden="true"></div>
  <p class="abs social-text">
    <span class="line-indent">Like and follow</span>
    <span class="line-indent org">Tubelight Restoration Works</span>
    on Glowboard for updates
  </p>

  <p class="abs food">FOOD &amp; DRINK<small>available for purchase</small></p>

  <footer class="abs contact-pill">info@tubelightworks.example | Call/Text 920-555-0172</footer>
</main>
</body>
</html>
```